Company or website name
- Copperfield Staff Bulletins
- Links to the website
- I 'breathe fresh life' into office workplaces with these inspirational wellbeing newsletters! =)
- Other Facts

```html
<!DOCTYPE html>
<html lang="en">
<head>
<meta charset="utf-8">
<title>Employee Well Being Program – Issue 12 2009</title>
<link rel="stylesheet" href="https://fonts.googleapis.com/css2?family=Pinyon+Script&family=Berkshire+Swash&family=Gelasio:wght@400;700&family=Arimo:wght@400;700&family=Tinos&family=Yesteryear&display=swap">
<style>
:root{
  --night:#0b0d2a;
  --aurora:#6a3fa8;
  --lime:#8dc63f;
  --issue:#f4e44a;
  --green-title:#5fd14a;
  --maroon:#2e0101;
  --cream:#f6efe4;
  --gold:#f4c64a;
  --butter:#fde7a8;
  --olive-green:#2e6a12;
  --stone:#e9e7de;
  --plum:#3a1850;
  --lavender:#cbcbf6;
  --orange:#f26a12;
  --peach:#fdc9a0;
  --mist:#ededed;
  --navy:#2b3592;
  --link-blue:#2a45a6;
  --ink:#1a1a1a;
  --black:#000;
}
*{margin:0;padding:0;box-sizing:border-box}
html,body{width:1200px;height:3318px;overflow:hidden;background:#fff}
.newsletter{position:relative;width:1200px;height:3318px;font-family:'Gelasio',Georgia,serif;color:var(--ink)}
.block{position:absolute;overflow:hidden}

/* masthead */
.masthead{left:0;top:0;width:1200px;height:264px;
  background:radial-gradient(ellipse 70% 45% at 50% 30%,#d9b6ff 0%,#8a58d0 30%,rgba(40,30,110,.6) 60%,transparent 80%),
             linear-gradient(180deg,#2a1f66 0%,var(--night) 70%,#05060f 100%)}
.masthead .issue{position:absolute;right:34px;top:14px;font-family:'Arimo',Arial,sans-serif;font-size:34px;color:var(--issue)}
.masthead h1{position:absolute;left:0;width:1200px;top:66px;text-align:center;font-family:'Pinyon Script',cursive;font-weight:400;font-size:92px;color:#fff;white-space:nowrap;
  text-shadow:0 0 2px #000,2px 2px 0 #333}
.masthead h1 .accent{color:var(--green-title)}
.rule{left:0;top:264px;width:1200px;height:17px;background:var(--lime)}

.intro{left:0;top:281px;width:1200px;height:249px;padding:12px 14px 0 14px;font-size:28px;line-height:38px;text-indent:30px}
.intro .drop{font-size:40px}

/* left column */
.interesting{left:0;top:530px;width:609px;height:1736px;background:var(--maroon);color:var(--cream);padding:10px 8px 0 8px;font-size:19.4px;line-height:25px}
.script-head{font-family:'Berkshire Swash',cursive;font-weight:400;text-align:center}
.interesting h2{color:var(--gold);font-size:38px;line-height:50px;margin-bottom:10px}
.interesting p{margin-bottom:25px}
.interesting .lead::first-letter{font-size:36px}
.interesting .lead{text-indent:30px}
.interesting .close{text-indent:20px}

.laugh{left:0;top:2266px;width:609px;height:277px;background:var(--peach);font-family:'Arimo',Arial,sans-serif}
.laugh .sun{position:absolute;left:22px;top:30px;width:228px;height:228px;border-radius:50%;background:radial-gradient(circle at 40% 35%,#fff8d6,#f4dc8a 70%,#d9b86a)}
.laugh h3{position:absolute;left:192px;top:18px;font-weight:400;font-size:37px}
.laugh p{position:absolute;left:300px;width:300px;font-size:31px;line-height:37px}

/* right column */
.did-know-head{left:611px;top:530px;width:589px;height:69px;background:var(--butter);text-align:center}
.did-know-head h2{font-size:42px;line-height:66px;color:var(--olive-green)}
.did-know-head .q{color:#e8d69a;font-family:'Arimo',sans-serif;font-size:48px}
.did-know-photo{left:611px;top:599px;width:589px;height:386px;background:radial-gradient(circle at 45% 30%,#ffffff 0%,#cfe3f5 14%,#3f7fc4 45%,#133c7a 100%)}
.did-know-text{left:611px;top:985px;width:589px;height:197px;background:var(--butter);padding:6px 12px 0 12px;font-size:21.3px;line-height:27.5px;color:#4a2a10}
.did-know-text .drop{font-size:40px;color:#7a1a10}

.swap{left:611px;top:1182px;width:589px;height:556px;background:var(--stone);padding:10px 14px 0 14px;font-size:23.3px;line-height:29.5px}
.swap h2{color:var(--plum);font-size:54px;line-height:70px;display:flex;align-items:center;justify-content:center;gap:14px}
.swap h2 svg{width:40px;height:40px}
.swap .sub{margin:14px 0 14px}
.swap .drop{font-size:40px}

.yummy{left:611px;top:1738px;width:589px;height:805px;background:var(--lavender);padding:10px 0 0 13px;font-family:'Arimo',Arial,sans-serif;font-size:20.5px;line-height:27.5px;white-space:nowrap}
.yummy h2{color:var(--orange);font-size:45px;font-weight:700;text-align:center;padding-right:13px;line-height:56px;margin-bottom:10px}
.yummy h3{font-weight:400;font-size:31px;line-height:40px}
.yummy .label{margin-bottom:27px}
.yummy ul{list-style:none;margin-bottom:28px}
.yummy ol{list-style:none;white-space:normal;padding-right:0;width:590px}
.fruit-photo{left:881px;top:1979px;width:309px;height:274px;background:radial-gradient(circle at 50% 55%,#e85a3a 0%,#f2b23f 25%,#9cc84a 42%,#f0e6dc 62%,#ffffff 90%)}

/* events */
.events{left:0;top:2543px;width:1200px;height:702px;background:var(--mist);padding:0 12px;font-family:'Tinos','Times New Roman',serif;font-size:24.4px;line-height:32px}
.events header{display:flex;align-items:center;justify-content:center;gap:10px;height:110px;margin:0 -12px}
.events header h2{font-weight:400;font-size:51px;color:var(--navy);margin:0 8px}
.clock{width:84px;height:84px}
.events p{margin-top:38px}
.events p:first-of-type{margin-top:42px}
.events .city{color:var(--link-blue)}

.quote{left:0;top:3245px;width:1200px;height:73px;background:var(--black);color:#fff;text-align:center;font-family:'Yesteryear',cursive;font-size:40px;line-height:70px}
</style>
</head>
<body>
<main class="newsletter">

  <header class="block masthead" role="img" aria-label="Night sky with purple aurora behind the newsletter title">
    <span class="issue">Issue:&nbsp; 12&nbsp; 2009</span>
    <h1>Employee <span class="accent">Well Being</span> Program</h1>
  </header>
  <div class="block rule"></div>

  <p class="block intro"><span class="drop">S</span>o much for 'winding down for the year' the silly season can be the most stressful of them all! For maximum wellbeing returns on minimum time investment, look no further than simple breathing. Take a deep breathe in, and then release it - along with any muscle tightness and stress. There you go, make breathing the gift to yourself to turn the silly season into the settled season.</p>

  <section class="block interesting">
    <h2 class="script-head">That’s Interesting....</h2>
    <p class="lead">Have you noticed some people seem to be able to eat what they like and still stay slim? Instead of secretly hating them, there are things we can learn about their habits and attitudes that allow them to stay lean. Here are the top 5 nutrition habits of naturally slim people:</p>
    <p>1.&nbsp; They only eat when truly hungry. There are so many cues around us to eat when we are not even physically hungry – we grab a few lollies while we’re at the desk, we have a biscuit from the kitchen with our morning tea, we eat a slice of cake because it’s a colleagues’ birthday…the list is endless! Unfortunately, this non-hungry snacking really does add up. Naturally slim people eat when they are truly physically hungry, and not because they are bored, frustrated, celebrating, with a group of people, stressed or because ‘it’s time to eat’. They listen to their own body and hunger rather than watching the clock, eating because other people expect them to, or eating because ‘it’s there’.</p>
    <p>2.&nbsp; Naturally slim and healthy people listen to their bodies. Some days we are hungrier than others, some days we crave different things. The body has its own innate wisdom, and some days our bodies require more fuel. Instead of dieting (trying to control or deny natural hunger,) naturally slim people honour their hunger and nurture their bodies. Our bodies know exactly what is needed at any given moment, and when we tune in we’re naturally led to the perfect foods for us.</p>
    <p>3.&nbsp; They enjoy a drink - and no, we are not talking about alcohol! Naturally slim people drink lots of water and stay well hydrated. They don’t confuse thirst with hunger. Most times when we think we are hungry, we are really thirsty, and our first response to this feeling should be to have a glass of water.</p>
    <p>4.&nbsp; Healthy people don’t do fad diets. Instead they eat in moderation, focus on nutrition and they don’t really think about food unless they are physically hungry. Some days they eat more, some days they eat less, all depending on what their body needs. Dieting is denying yourself, and truly healthy people, inside and out, would never deny themselves. Instead they honour and nourish their bodies with the best quality food. Which leads to the final point…</p>
    <p>5.&nbsp; Naturally slim and healthy people get pleasure for example, when they eat a salad they think of all the vitamins, minerals and nutrients that they are providing their body and they feel good taking care of themselves. They don’t see a salad as deprivation at all, instead they feel nourished. Naturally slim people see food as fuel. They seek out the highest quality fuel, and gain pleasure nourishing each cell with the best quality nutrients.</p>
    <p class="close">When it comes down to it, no one is “naturally” slim at all. We all have the choice of abusing and destroying our bodies, or nurturing and creating health. It all lies in our approach and thoughts and behaviours – that’s what creates our reality in all areas of life. Our body is always a reflection of what’s going on inside, and when we have positive thoughts and a healthy attitude towards food, we’re naturally guided to the best fuel to nourish ourselves and keep us at our perfect weight.</p>
  </section>

  <section class="block laugh">
    <div class="sun" role="img" aria-label="Cheerful cartoon smiley illustration"></div>
    <h3>Ha! Ha! Ha!</h3>
    <p style="top:78px">“Waiter! This coffee tastes like mud.”</p>
    <p style="top:188px">“Yes sir, it’s fresh ground.”</p>
  </section>

  <div class="block did-know-head">
    <h2 class="script-head"><span class="q">? ?</span> Did You Know? <span class="q">? ?</span></h2>
  </div>
  <div class="block did-know-photo" role="img" aria-label="Photo of a woman drinking from a water bottle against a bright sunny sky"></div>
  <p class="block did-know-text"><span class="drop">T</span>he human body is comprised of 80% water and a mere 2% loss in body water can reduce your energy levels by 20 per cent! The effects of dehydration are poor concentration, tiredness and headaches, and you simply can’t think as efficiently when you are dehydrated. So drink up !</p>

  <section class="block swap">
    <h2 class="script-head">
      <svg viewBox="0 0 40 40" aria-hidden="true"><path d="M32 30 C30 14 20 10 10 14" fill="none" stroke="#1a1a1a" stroke-width="4"/><path d="M4 14 L14 6 L14 22 Z" fill="#1a1a1a"/></svg>
      Swap This!
      <svg viewBox="0 0 40 40" aria-hidden="true"><path d="M8 10 C10 26 20 30 30 26" fill="none" stroke="#1a1a1a" stroke-width="4"/><path d="M36 26 L26 34 L26 18 Z" fill="#1a1a1a"/></svg>
    </h2>
    <p class="sub">Coffee for green tea:</p>
    <p><span class="drop">A</span> skim latte has around 100-200 calories, and is a hit of false energy. Caffeine can enervate your body, and in the long term it leaves you fatigued. Herbal teas have only 5 calories, and each has their own natural benefits for your body. Green tea does have some caffeine (around 1/3 of the amount in coffee) but is also a powerful anti-oxidant, chamomile has calming properties, ginger root is excellent for improving circulation and peppermint tea aids digestion and is good for stress relief.</p>
  </section>

  <section class="block yummy">
    <h2>Yummy!</h2>
    <h3>Tasty Tuscan Chicken</h3>
    <p class="label">INGREDIENTS:</p>
    <ul>
      <li>- 1 Punnet grape tomatoes</li>
      <li>- 1/2 cup (50g) pimento stuffed green olives</li>
      <li>- 2 tbs olive oil</li>
      <li>- Juice of 1/2 lemon</li>
      <li>- 2 Chicken breast fillets</li>
      <li>- 1 tbs capers</li>
      <li>- ½ cup</li>
      <li>- Rice</li>
      <li>- Basil leaves</li>
      <li>- Brown rice</li>
      <li>- Green salad to serve</li>
    </ul>
    <p class="label">METHOD:</p>
    <ol>
      <li>1. Preheat oven to 180°C. Combine tomatoes, olives, capers, olive oil and lemon juice in a bowl.</li>
      <li>2. Season chicken to taste and fry in a non stick pan for 3 minutes each side, until golden brown. Transfer to a baking pan.</li>
      <li>3. Pour the tomato mixture over the chicken in the baking pan and season to taste. Bake for 15 minutes.</li>
      <li>4. Top with a few basil leaves and serve with brown rice and leaves.</li>
    </ol>
  </section>
  <div class="block fruit-photo" role="img" aria-label="Photo of cupped hands holding fresh fruit"></div>

  <section class="block events">
    <header>
      <svg class="clock" viewBox="0 0 84 84" aria-hidden="true"><circle cx="42" cy="42" r="38" fill="none" stroke="#b5b5b5" stroke-width="3"/><path d="M20 40 L42 44 L30 56" fill="none" stroke="#9a9a9a" stroke-width="4"/></svg>
      <svg class="clock" viewBox="0 0 84 84" aria-hidden="true"><circle cx="42" cy="42" r="38" fill="none" stroke="#b5b5b5" stroke-width="3"/><path d="M42 16 L42 44 L26 44" fill="none" stroke="#9a9a9a" stroke-width="4"/></svg>
      <svg class="clock" viewBox="0 0 84 84" aria-hidden="true"><circle cx="42" cy="42" r="38" fill="none" stroke="#b5b5b5" stroke-width="3"/><path d="M30 24 L40 52 L60 34" fill="none" stroke="#9a9a9a" stroke-width="4"/></svg>
      <h2>What’s on this weekend?</h2>
      <svg class="clock" viewBox="0 0 84 84" aria-hidden="true"><circle cx="42" cy="42" r="38" fill="none" stroke="#b5b5b5" stroke-width="3"/><path d="M58 28 L36 42 L52 58" fill="none" stroke="#9a9a9a" stroke-width="4"/></svg>
      <svg class="clock" viewBox="0 0 84 84" aria-hidden="true"><circle cx="42" cy="42" r="38" fill="none" stroke="#b5b5b5" stroke-width="3"/><path d="M42 60 L42 30 L56 40" fill="none" stroke="#9a9a9a" stroke-width="4"/></svg>
      <svg class="clock" viewBox="0 0 84 84" aria-hidden="true"><circle cx="42" cy="42" r="38" fill="none" stroke="#b5b5b5" stroke-width="3"/><path d="M24 56 L46 34 L58 34" fill="none" stroke="#9a9a9a" stroke-width="4"/></svg>
    </header>
    <p><span class="city">Sydney 28th-</span> Harbourside Christmas Concert A family concert with performances from The Pyjama Twins. Convention Centre Forecourt, Harbourside Quay from 8pm, free.</p>
    <p><span class="city">Melbourne 28th and 29th-</span> November Urban Dash The exciting physical and mental urban adventure challenge is back on 28-29 November when teams of three will run, ride, kayak, climb and abseil across a course that’s only revealed to them hours before they begin. For more information call 1800 555 012.</p>
    <p><span class="city">Canberra 28 &amp; 29th-</span> Southvale Festival On Saturday 28 November, the Big 21st Birthday Bash Street Party will be held in Marrow Street. On Sunday 29 November, The Southvale Festival will celebrate 21 years with a free festival featuring live music, a children’s show, skateboarding and rollerblading, fireworks, market stalls and more in Southvale Town Park.</p>
    <p><span class="city">Brisbane 28 &amp; 29-</span> Santa Celebration Activities include a jumping castle, a train simulator, art and craft, a screening of the Snowline Express and more. There will also be a visit from Santa. Activities are free after general museum entry. The Ironworks Rail Museum, Depot St, Eastbridge.</p>
  </section>

  <footer class="block quote">“There are no shortcuts to any place worth going” - Vera Linwood</footer>

</main>
</body>
</html>
```